Business Cards

Business card design for my company.
I would like the card's background colour to be black. You can also see our web site to get an idea of our brand. https://www.dlqmarrowfield.com.au/
- Name
- Email

```html
<!DOCTYPE html>
<html lang="en">
<head>
<meta charset="utf-8">
<title>DLQ Marrowfield – Business Cards</title>
<link href="https://fonts.googleapis.com/css2?family=Montserrat:ital,wght@0,400;0,600;0,700;1,400;1,500&display=swap" rel="stylesheet">
<style>
  :root {
    --bg: #eef3f6;
    --card: #000000;
    --green: #0e9440;
    --white: #ffffff;
  }
  html, body { margin: 0; padding: 0; overflow: hidden; }
  body { width: 1200px; height: 675px; background: var(--bg); position: relative; font-family: "Montserrat", sans-serif; }
  .cards { position: absolute; inset: 0; }
  .card-shape { filter: drop-shadow(3px 5px 5px rgba(0,0,0,0.35)); }
  .wordmark {
    position: absolute; color: var(--white); font-weight: 700;
    letter-spacing: 0.5px; text-align: center; white-space: nowrap;
  }
  .wordmark--front { left: 150px; width: 400px; top: 356px; font-size: 28px; }
  .wordmark--back { left: 626px; width: 202px; top: 366px; font-size: 16px; }
  .divider { position: absolute; left: 841px; top: 305px; width: 2px; height: 136px; background: var(--green); }
  .contact { position: absolute; left: 856px; top: 308px; color: var(--white); }
  .contact__name { font-size: 15px; font-weight: 700; letter-spacing: 0.3px; margin: 0; }
  .contact__role { font-size: 11.5px; font-style: italic; color: var(--green); margin: 2px 0 14px; }
  .contact__list { list-style: none; margin: 0; padding: 0; font-size: 11.5px; }
  .contact__list li { display: flex; align-items: center; gap: 6px; height: 16px; }
  .contact__list svg { width: 12px; height: 12px; fill: var(--green); flex: none; }
  .contact__place { font-size: 11.5px; font-style: italic; font-weight: 500; margin-top: 16px; }
  .contact__place .sep { color: var(--green); margin: 0 2px; }
</style>
</head>
<body>
  <svg class="cards" width="1200" height="675" viewBox="0 0 1200 675">
    <g class="card-shape">
      <polygon fill="var(--green)" points="112,284 233,202 589,297 589,474 112,474"/>
      <polygon fill="var(--card)" points="112,306 237,221 589,316 589,474 112,474"/>
    </g>
    <g class="card-shape">
      <polygon fill="var(--green)" points="611,294 967,201 1089,284 1089,474 611,474"/>
      <polygon fill="var(--card)" points="611,313 963,220 1089,305 1089,474 611,474"/>
    </g>
  </svg>

  <div class="wordmark wordmark--front">DLQ MARROWFIELD</div>
  <div class="wordmark wordmark--back">DLQ MARROWFIELD</div>

  <div class="divider"></div>
  <div class="contact">
    <p class="contact__name">DEAN HALLOWAY</p>
    <p class="contact__role">General Manager</p>
    <ul class="contact__list">
      <li><svg viewBox="0 0 24 24"><path d="M6.6 10.8a15 15 0 0 0 6.6 6.6l2.2-2.2a1 1 0 0 1 1-.25 11.4 11.4 0 0 0 3.6.57 1 1 0 0 1 1 1V20a1 1 0 0 1-1 1A17 17 0 0 1 3 4a1 1 0 0 1 1-1h3.5a1 1 0 0 1 1 1c0 1.25.2 2.45.57 3.57a1 1 0 0 1-.25 1z"/></svg>0400 123 456</li>
      <li><svg viewBox="0 0 24 24"><path d="M2 5h20v14H2z M2 5l10 8 10-8" fill="var(--green)" stroke="var(--card)" stroke-width="1.5"/></svg>info@dlqmarrowfield.com.au</li>
      <li><svg viewBox="0 0 24 24"><circle cx="12" cy="12" r="10"/><path d="M2 12h20M12 2c3 3 3 17 0 20M12 2c-3 3-3 17 0 20" fill="none" stroke="var(--card)" stroke-width="1.5"/></svg>www.dlqmarrowfield.com.au</li>
    </ul>
    <div class="contact__place">HOBART <span class="sep">|</span> TASMANIA <span class="sep">|</span> AUSTRALIA</div>
  </div>
</body>
</html>
```